Business Card Design Project

Im an electrician and my company name is Kestrel Electrical
My main work is installing Lighting and Power Points, Home Theater Systems, TVS, Phones and Data
Im looking a business card, something nice, clean, modern and not to cluttered
Im open to sugestions
I dont mind if the "Services" is on the back on the business card
colours black, grey, white or the blue colour of my logo are prefered but not compulsory
any questions just message me
and please make it so if i need to edit the writing can do it easy. maybe by making it a seperate layer ?
My Details are.
Name - Peter Halloran
Job Title - Licenced Electrician
Mobile - 027 583 2174
Email - peter@kestrelelectrical.co.nz
Web - www.kestrelelectrical.co.nz
Services
Residential / Commercial
Lighting & Power
Heating & Ventilation
Automation
Phone & Data
Home Cinema
Sound Systems
TV, Antenna & Satellite
Digital Upgrades

```html
<!DOCTYPE html>
<html lang="en">
<head>
<meta charset="utf-8">
<title>Kestrel Electrical — Business Card</title>
<link href="https://fonts.googleapis.com/css2?family=Barlow:wght@400;500;600&display=swap" rel="stylesheet">
<style>
  :root {
    --teal: #12a9c6;
    --slate: #5a6169;
    --ink: #4a5058;
    --paper: #ffffff;
    --backdrop: #e9ebed;
  }
  * { box-sizing: border-box; margin: 0; padding: 0; }
  html, body {
    width: 1200px; height: 900px; overflow: hidden;
    background: var(--backdrop);
    font-family: "Barlow", Arial, sans-serif;
  }
  .sheet {
    width: 1200px; height: 900px;
    display: flex; flex-direction: column; align-items: center; justify-content: center;
    gap: 40px;
  }
  .card {
    width: 630px; height: 360px;
    position: relative; overflow: hidden;
    box-shadow: 0 6px 18px rgba(0,0,0,0.18);
  }

  /* Back of card */
  .card-back { background: var(--teal); }
  .card-back .brand-mark {
    position: absolute; left: 0; right: 0; top: 88px;
    display: flex; align-items: center; justify-content: center; gap: 14px;
    color: var(--paper); font-weight: 600; font-size: 38px; letter-spacing: 1px;
  }
  .brand-mark .square { width: 22px; height: 22px; background: currentColor; }
  .services {
    position: absolute; left: 0; right: 0; bottom: 0; height: 128px;
    background: var(--slate);
    display: flex; flex-direction: column; justify-content: center; align-items: center;
    color: var(--paper); font-size: 17px; line-height: 1.5; letter-spacing: 0.4px;
  }
  .services::before, .services::after {
    content: ""; position: absolute; left: 22px; right: 22px; height: 1px;
    background: var(--teal);
  }
  .services::before { top: 14px; }
  .services::after { bottom: 14px; }

  /* Front of card */
  .card-front { background: var(--paper); }
  .card-front .brand-mark {
    position: absolute; left: 44px; top: 46px;
    display: flex; align-items: center; gap: 12px;
    color: var(--teal); font-weight: 600; font-size: 30px; letter-spacing: 1px;
  }
  .contact {
    position: absolute; left: 300px; top: 170px;
  }
  .contact .name {
    color: var(--ink); font-weight: 500; font-size: 27px; letter-spacing: 1px;
    text-transform: uppercase;
  }
  .contact .role {
    color: var(--teal); font-size: 17px; letter-spacing: 0.5px; margin-top: 2px;
  }
  .details {
    margin-top: 26px; margin-left: -72px;
    display: grid; grid-template-columns: 64px auto; column-gap: 10px;
    font-size: 18px; line-height: 1.35; letter-spacing: 0.4px;
  }
  .details dt { color: var(--teal); text-align: right; }
  .details dd { color: var(--ink); }
</style>
</head>
<body>
<main class="sheet">
  <section class="card card-back" aria-label="Card back">
    <div class="brand-mark"><span class="square"></span><span>Kestrel Electrical</span></div>
    <div class="services">
      <p>Residential / Commercial • Lighting &amp; Power • Heating &amp; Ventilation</p>
      <p>Automation • Phone &amp; Data • Home Cinema • Sound Systems</p>
      <p>TV, Antenna &amp; Satellite • Digital Upgrades</p>
    </div>
  </section>

  <section class="card card-front" aria-label="Card front">
    <div class="brand-mark"><span class="square"></span><span>Kestrel Electrical</span></div>
    <div class="contact">
      <h1 class="name">Peter Halloran</h1>
      <p class="role">Licenced Electrician</p>
      <dl class="details">
        <dt>mobile</dt><dd>027 583 2174</dd>
        <dt>email</dt><dd>peter@kestrelelectrical.co.nz</dd>
        <dt>site</dt><dd>www.kestrelelectrical.co.nz</dd>
      </dl>
    </div>
  </section>
</main>
</body>
</html>
```